BRIVETTA Need a luxury modern business card designed.

Need a luxury modern business card designed. refer to the uploaded files for the company name and logo in the zip file under source files. i will making my descion on monday. so please send in before then so if we need to edit we will have the time. we have a trade show coming up and im on a deadline for printer.

Target Market(s)

high end clients

Contact Information for Business Card

Company nAme and logo. Calvin Moross Co-Founder / Project Manager Office # 416-555-7391 Cell # 416-555-0186 BRIVETTA.CA Calvin@brivetta.ca

Font styles to use
Other font styles liked:
• Modern

Requirements
Must have
• Company name and logo, contact info, using the black, gold and white color scheme.

```html
<!DOCTYPE html>
<html lang="en">
<head>
<meta charset="utf-8">
<title>Brivetta Business Card</title>
<link rel="stylesheet" href="https://fonts.googleapis.com/css2?family=Montserrat:wght@400;500;600&display=swap">
<style>
  :root {
    --bg: #1c1c1c;
    --charcoal: #333333;
    --ink: #2b2b2b;
    --gold: #a8966a;
    --white: #ffffff;
  }
  * { box-sizing: border-box; margin: 0; padding: 0; }
  html, body { width: 1200px; height: 900px; overflow: hidden; }
  body {
    background: var(--bg);
    font-family: "Montserrat", sans-serif;
    display: flex;
    flex-direction: column;
    align-items: center;
    justify-content: center;
    gap: 50px;
  }
  .card {
    position: relative;
    width: 630px;
    height: 360px;
    overflow: hidden;
    box-shadow: 0 12px 30px rgba(0,0,0,.45);
  }
  .brand-name {
    font-weight: 400;
    letter-spacing: .22em;
    white-space: nowrap;
  }

  /* Back side */
  .card--back {
    background: var(--charcoal);
    display: flex;
    align-items: center;
    justify-content: center;
  }
  .card--back .brand-name { font-size: 34px; color: var(--white); }

  /* Front side */
  .card--front { background: var(--white); }
  .front-band {
    position: absolute;
    left: 0; right: 0; bottom: 0;
    height: 150px;
    background: var(--charcoal);
  }
  .front-rule {
    position: absolute;
    left: 0; right: 0;
    bottom: 158px;
    height: 3px;
    background: var(--gold);
  }
  .front-brand {
    position: absolute;
    left: 40px;
    top: 62px;
    display: flex;
    align-items: center;
    gap: 14px;
  }
  .front-brand .mark-square {
    width: 22px; height: 22px;
    background: var(--gold);
  }
  .front-brand .brand-name { font-size: 30px; color: var(--ink); }
  .holder {
    position: absolute;
    right: 40px;
    top: 112px;
    text-align: right;
  }
  .holder__name {
    font-size: 22px;
    font-weight: 600;
    letter-spacing: .05em;
    color: var(--gold);
  }
  .holder__title {
    margin-top: 4px;
    font-size: 15px;
    font-weight: 500;
    color: var(--ink);
  }
  .contacts {
    position: absolute;
    right: 30px;
    bottom: 22px;
    list-style: none;
    display: flex;
    flex-direction: column;
    gap: 4px;
  }
  .contacts li {
    display: flex;
    align-items: center;
    justify-content: flex-end;
    gap: 10px;
    color: var(--white);
    font-size: 15px;
    font-weight: 500;
  }
  .contacts svg { width: 16px; height: 16px; flex: none; }
  .contacts .accent { color: var(--gold); }
</style>
</head>
<body>

  <section class="card card--back" aria-label="Card back">
    <span class="brand-name">BRIVETTA</span>
  </section>

  <section class="card card--front" aria-label="Card front">
    <div class="front-rule"></div>
    <div class="front-band"></div>

    <div class="front-brand">
      <span class="mark-square"></span>
      <span class="brand-name">BRIVETTA</span>
    </div>

    <div class="holder">
      <p class="holder__name">CALVIN MOROSS</p>
      <p class="holder__title">Co-Founder | Project Manager</p>
    </div>

    <ul class="contacts">
      <li>416-555-7391
        <svg viewBox="0 0 24 24" fill="none" stroke="var(--gold)" stroke-width="2"><path d="M5 3h4l2 5-3 2a12 12 0 0 0 6 6l2-3 5 2v4a2 2 0 0 1-2 2A17 17 0 0 1 3 5a2 2 0 0 1 2-2z"/></svg>
      </li>
      <li>416-555-0186
        <svg viewBox="0 0 24 24" fill="none" stroke="var(--gold)" stroke-width="2"><rect x="7" y="2" width="10" height="20" rx="2"/><line x1="11" y1="18" x2="13" y2="18"/></svg>
      </li>
      <li>Calvin@brivetta.ca
        <svg viewBox="0 0 24 24" fill="none" stroke="var(--gold)" stroke-width="2"><rect x="2" y="5" width="20" height="14"/><path d="M2 5l10 8 10-8"/></svg>
      </li>
      <li><span>WWW.<span class="accent">BRIVETTA</span>.CA</span>
        <svg viewBox="0 0 24 24" fill="none" stroke="var(--gold)" stroke-width="2"><circle cx="12" cy="12" r="10"/><path d="M2 12h20M12 2a15 15 0 0 1 0 20M12 2a15 15 0 0 0 0 20"/></svg>
      </li>
    </ul>
  </section>

</body>
</html>
```